Marrowgate Bidding Consortium
Auctioneers & Appraiser
Marrowgate Bidding Consortium - Antiques and Collectibles
Creative Brief
Antiques and Collectibles
www.marrowBids.example
Marrowgate Bidding Consortium sales specialists provide expertise and detailed understanding of the current markets along with professional accuracy and advice to our clients. In addition, Tamsworth's Trusts & Estates department offers various services to facilitate any full estate sale, and a willingness to work at the client's discretion. The auction house's has allowed MBC's to expand into the China market. This alliance has enhanced MBC's capability to maximize the sale potential in an international market, while maintaining the company's unique standard of one-on-one client service. Today, the Auction house is furthering their growth with a greater concentration in specialized departments. As a leading regional auction house, MBC's is progressing forward with the expanding global market, and is looking to the future to provide services which MBC's clients require and deserve
below header
http://www.vendrelhall.example/
http://oddlotgoods.example/
http://www.hollowaysbids.example/

```html
<!DOCTYPE html>
<html lang="en">
<head>
<meta charset="utf-8">
<title>Marrowgate Bidding Consortium - Antiques and Collectibles</title>
<link rel="stylesheet" href="https://fonts.googleapis.com/css2?family=Oswald:wght@400;500;600&family=Open+Sans:wght@400;600;700&family=Playfair+Display:wght@400&display=swap">
<style>
:root{
  --ink:#141210;
  --topbar:#1b1a19;
  --nav:#2b2a29;
  --nav-line:#3d3b39;
  --red:#b1121b;
  --red-deep:#5b0b0e;
  --red-dark:#3a0608;
  --gold:#e0a21c;
  --gold-soft:rgba(196,140,24,.82);
  --cream:#f3ead6;
  --muted:#9a948c;
  --white:#ffffff;
}
*{box-sizing:border-box;margin:0;padding:0}
html,body{width:1200px;height:667px;overflow:hidden;background:var(--ink)}
body{font-family:"Open Sans",Arial,sans-serif;color:var(--white);position:relative}

.site-header{position:absolute;left:0;top:0;width:1200px;height:41px;background:var(--topbar);display:flex;align-items:center;padding:0 96px}
.brand{display:flex;align-items:center;gap:12px}
.brand-name{font-family:"Oswald",sans-serif;font-weight:600;font-size:19px;color:var(--gold);letter-spacing:.5px}
.brand-tag{font-family:"Oswald",sans-serif;font-weight:400;font-size:10px;color:var(--muted);letter-spacing:1px;border-left:1px solid #4a4744;padding-left:10px}
.header-tools{margin-left:auto;display:flex;align-items:center;gap:6px}
.social-dot{width:20px;height:20px;border-radius:50%;background:#5a5855}
.search{margin-left:8px;display:flex;align-items:center;width:158px;height:24px;background:#3a3836;border:1px solid #4c4a47;padding:0 6px;font-size:9px;color:#aaa;letter-spacing:.5px}
.search svg{margin-left:auto}

.main-nav{position:absolute;left:0;top:41px;width:1200px;height:29px;background:var(--nav);border-bottom:1px solid var(--nav-line)}
.main-nav ul{list-style:none;display:flex;height:100%;padding-left:96px}
.main-nav li{font-family:"Open Sans",sans-serif;font-size:10px;font-weight:600;letter-spacing:.3px;padding:0 13px;display:flex;align-items:center;color:#e8e4de}
.main-nav li.is-active{background:var(--red)}

.hero{position:absolute;left:0;top:70px;width:1200px;height:417px;overflow:hidden}
.hero-photo{position:absolute;inset:0;background:
  radial-gradient(ellipse 40% 60% at 62% 55%,rgba(176,122,70,.55),transparent 70%),
  radial-gradient(ellipse 30% 50% at 88% 30%,rgba(120,86,50,.5),transparent 70%),
  linear-gradient(90deg,#2a1c12 0%,#3d2a1a 45%,#4a3320 70%,#221710 100%)}
.hero-panel{position:absolute;left:0;top:139px;width:523px;height:237px;background:var(--gold-soft);padding:6px 18px 0 96px}
.hero-title{font-family:"Playfair Display",serif;font-weight:400;font-size:52px;line-height:52px;color:var(--white);white-space:nowrap}
.hero-text{margin-top:8px;font-size:10.4px;line-height:15px;color:var(--cream)}
.hero-more{position:absolute;right:12px;bottom:18px;font-family:"Oswald",sans-serif;font-size:10.5px;letter-spacing:.4px;color:var(--white)}
.hero-more span{color:#fff3c8;margin-right:4px}
.slider-arrow{position:absolute;top:240px;width:42px;height:42px;border-radius:50%;background:rgba(40,36,32,.75);display:flex;align-items:center;justify-content:center}
.slider-arrow.prev{left:22px}
.slider-arrow.next{right:22px}

.feature-band{position:absolute;left:0;top:487px;width:1200px;height:149px;background:linear-gradient(180deg,var(--red-deep) 0%,var(--red-dark) 100%);border-top:3px solid #7a0f14}
.tiles{position:absolute;left:96px;top:10px;display:flex;gap:6px}
.tile{width:186px}
.tile-title{height:22px;background:#241f1d;font-family:"Oswald",sans-serif;font-weight:500;font-size:12.5px;letter-spacing:.4px;padding:2px 7px;color:var(--white)}
.tile.is-featured .tile-title{background:var(--gold);color:#2a1a05}
.tile-image{height:96px;border:2px solid #1b1413;border-top:0}
.img-collections{background:linear-gradient(135deg,#2c2018,#6b4a2e 55%,#1d1610)}
.img-events{background:linear-gradient(135deg,#3a2a1e,#8c6a46 50%,#2a1f18)}
.img-magazine{background:linear-gradient(160deg,#1f1a16,#5a4836 50%,#c9a878)}
.img-catalogues{background:linear-gradient(135deg,#4a2a22,#b08c74 55%,#3b241c)}

.newsletter{position:absolute;left:868px;top:10px;width:300px}
.newsletter h2{font-family:"Oswald",sans-serif;font-weight:400;font-size:17px;color:var(--gold)}
.newsletter .field{margin-top:10px;width:228px;height:22px;background:#1a0d0d;border:1px solid #5d2a2a;font-size:9px;color:#8d7e7a;padding:4px 8px}
.newsletter .signup{margin-top:10px;width:66px;height:22px;background:var(--gold);color:#2a1a05;font-family:"Oswald",sans-serif;font-weight:600;font-size:11px;display:flex;align-items:center;justify-content:center}

.site-footer{position:absolute;left:0;top:636px;width:1200px;height:31px;background:#120f0e;display:flex;align-items:center;padding:0 96px;font-size:9.5px;color:var(--muted)}
.follow{margin-left:auto;display:flex;align-items:center;gap:5px;color:#d8d2ca}
.follow span{margin-right:4px}
.follow .social-dot{background:#e8e4de;width:19px;height:19px}
</style>
</head>
<body>

<header class="site-header">
  <div class="brand">
    <span class="brand-name">MARROWGATE</span>
    <span class="brand-tag">AUCTIONEERS &amp; APPRAISER</span>
  </div>
  <div class="header-tools">
    <span class="social-dot"></span>
    <span class="social-dot"></span>
    <span class="social-dot"></span>
    <span class="social-dot"></span>
    <div class="search">SEARCH
      <svg width="11" height="11" viewBox="0 0 11 11"><circle cx="4.5" cy="4.5" r="3.3" fill="none" stroke="#ddd" stroke-width="1.4"/><line x1="7" y1="7" x2="10" y2="10" stroke="#ddd" stroke-width="1.6"/></svg>
    </div>
  </div>
</header>

<nav class="main-nav">
  <ul>
    <li class="is-active">HOME</li>
    <li>MY TAMSWORTH'S</li>
    <li>AUCTIONS</li>
    <li>BUYING</li>
    <li>SELLING</li>
    <li>DEPARTMENTS</li>
    <li>CATALOGUES</li>
    <li>SERVICES</li>
    <li>NEWS</li>
    <li>EVENTS</li>
    <li>INFORMATION</li>
    <li>CONTACT</li>
  </ul>
</nav>

<section class="hero">
  <div class="hero-photo" role="img" aria-label="Photo of a couple admiring an antique painted globe in a dim antiques shop"></div>
  <div class="hero-panel">
    <h1 class="hero-title">Antiques and<br>Collectibles</h1>
    <p class="hero-text">Marrowgate Bidding Consortium sales specialists provide expertise and detailed understanding of the current markets along with professional accuracy and advice to our clients. In addition, Tamsworth's Trusts &amp; Estates department offers various services to facilitate any full estate sale, and a willingness to work at the client's discretion.</p>
    <div class="hero-more"><span>&raquo;</span>CLICK FOR MORE INFORMATION</div>
  </div>
  <div class="slider-arrow prev"><svg width="14" height="16" viewBox="0 0 14 16"><path d="M11 1 L3 8 L11 15" fill="none" stroke="#fff" stroke-width="3"/></svg></div>
  <div class="slider-arrow next"><svg width="14" height="16" viewBox="0 0 14 16"><path d="M3 1 L11 8 L3 15" fill="none" stroke="#fff" stroke-width="3"/></svg></div>
</section>

<section class="feature-band">
  <div class="tiles">
    <article class="tile is-featured">
      <h3 class="tile-title">FEATURED COLLECTIONS</h3>
      <div class="tile-image img-collections" role="img" aria-label="Photo of a candlelit antique interior"></div>
    </article>
    <article class="tile">
      <h3 class="tile-title">EVENTS</h3>
      <div class="tile-image img-events" role="img" aria-label="Photo of guests at an auction event"></div>
    </article>
    <article class="tile">
      <h3 class="tile-title">OUR MAGAZINE</h3>
      <div class="tile-image img-magazine" role="img" aria-label="Photo of an antiques magazine cover"></div>
    </article>
    <article class="tile">
      <h3 class="tile-title">CATALOGUES</h3>
      <div class="tile-image img-catalogues" role="img" aria-label="Photo of collectible catalogue items"></div>
    </article>
  </div>
  <div class="newsletter">
    <h2>Newsletter Sign Up</h2>
    <div class="field">enter your email address</div>
    <div class="signup">SIGN UP</div>
  </div>
</section>

<footer class="site-footer">
  <p>2013 &copy; www.marrowBids.example. All Rights Reserved. &nbsp;PHONE: 215-555-0147</p>
  <div class="follow">
    <span>Follow us on:</span>
    <span class="social-dot"></span>
    <span class="social-dot"></span>
    <span class="social-dot"></span>
    <span class="social-dot"></span>
  </div>
</footer>

</body>
</html>
```